We are needing a bookcover for a reprint of our book "Whispers Beneath the Amber Horizon". It takes a look at the geologic formation found in the great plains. Our original cover was colorful and showed rock layers. Something similar but different and eye catching would be great. a geologic cross section showing various layers or possibly some different rocks/soils. We are really open to suggestions attached is the current book cover with the colored layers and the cover from the 80s.

Target Market(s)

Adult Readers

Industry/Entity Type

Nonprofit retail - science - nature

Requirements
Must have
• Geology or rock layers
Nice to have
• Books title, Geologic cross section
Should not have
• People or animals, no photos prefer sketch

```html
<!DOCTYPE html>
<html lang="en">
<head>
<meta charset="utf-8">
<title>Whispers Beneath the Amber Horizon — Book Cover</title>
<link rel="stylesheet" href="https://fonts.googleapis.com/css2?family=Cinzel:wght@500;600&display=swap">
<style>
  :root {
    --page-bg: #e9dfcf;
    --cover-bg: #1e1c1a;
    --title-gold: #ecc98c;
    --rule-dim: #8a4a1c;
    --rule-bright: #f07a24;
    --layer-red: #b8231d;
    --layer-orange: #f0761a;
    --layer-amber: #f6a43a;
    --layer-brown: #5a3a2c;
    --layer-sand: #c9ae86;
  }
  * { margin: 0; padding: 0; box-sizing: border-box; }
  html, body {
    width: 1200px;
    height: 1200px;
    overflow: hidden;
    background: var(--page-bg);
  }
  .canvas {
    position: relative;
    width: 1200px;
    height: 1200px;
  }
  .book-cover {
    position: absolute;
    left: 200px;
    top: 80px;
    width: 800px;
    height: 1040px;
    background: var(--cover-bg);
    font-family: "Cinzel", "Trajan Pro", serif;
    color: var(--title-gold);
    overflow: hidden;
  }
  .title-rule {
    position: absolute;
    left: 130px;
    width: 633px;
    height: 3px;
    background: linear-gradient(to right,
      var(--rule-dim) 0%, var(--rule-bright) 15%,
      var(--rule-bright) 82%, var(--rule-dim) 100%);
  }
  .title-rule--top { top: 73px; }
  .title-rule--bottom { top: 411px; }
  .title-block {
    position: absolute;
    left: 130px;
    width: 633px;
    text-align: center;
  }
  .title-kicker {
    top: 88px;
    font-size: 38px;
    font-weight: 500;
    letter-spacing: 2px;
    line-height: 44px;
  }
  .title-main {
    top: 140px;
    font-size: 88px;
    font-weight: 600;
    line-height: 94px;
    letter-spacing: 1px;
  }
  .title-tail {
    top: 432px;
    font-size: 38px;
    font-weight: 500;
    letter-spacing: 2px;
    line-height: 44px;
  }
  .strata-art {
    position: absolute;
    left: 205px;
    top: 511px;
    width: 595px;
    height: 444px;
    background: linear-gradient(to bottom,
      var(--layer-sand) 0%,
      var(--layer-red) 14%,
      var(--layer-orange) 30%,
      var(--layer-red) 44%,
      var(--layer-amber) 58%,
      var(--layer-orange) 70%,
      var(--layer-brown) 82%,
      var(--layer-red) 89%,
      var(--layer-sand) 100%);
  }
</style>
</head>
<body>
  <main class="canvas">
    <section class="book-cover">
      <div class="title-rule title-rule--top"></div>
      <p class="title-block title-kicker">WHISPERS</p>
      <h1 class="title-block title-main">BENEATH<br>THE AMBER</h1>
      <div class="title-rule title-rule--bottom"></div>
      <p class="title-block title-tail">HORIZON</p>
      <div class="strata-art" role="img" aria-label="Illustration of layered sedimentary rock strata in red, orange, amber and brown bands"></div>
    </section>
  </main>
</body>
</html>
```